Lantern Walk for Kids

I am an intern at Pellham Ridge Community College, and Student Forum is hosting a Lantern Walk for Kids in the Johnson County area. I am looking for a digital flyer to use for the event. Here are details for this year's event and info from last year. If you have any questions, please let me know. Last year's flyer is attached below.

Date: Friday, Oct. 25th, 2019
Location: Morrow Hall (Ground Floor)
Theme: Owls & Moons
Exciting Activities Include:
-(Glowing) Footsteps showing the path the kids should go?
-Face painting
-Cotton Candy
-Fog Machine w/bubbles
-Candy sponsorship (Fairlot or Oak Basket)
-Encouraging the community to bring food donations for PRCC Food Pantry

```html
<!DOCTYPE html>
<html lang="en">
<head>
<meta charset="utf-8">
<title>Lantern Walk for Kids – Student Forum</title>
<link href="https://fonts.googleapis.com/css2?family=Cinzel:wght@500;700&family=Great+Vibes&family=Montserrat:wght@600;800&family=Oswald:wght@600;700&display=swap" rel="stylesheet">
<style>
  :root {
    --ink: #0d0b09;
    --orange: #ef9a1c;
    --parchment-light: #f3ddb0;
    --parchment-dark: #d8b47c;
    --moon: #f6e3a8;
    --shadow: rgba(60, 50, 40, 0.45);
    --logo-grey: #3a3632;
  }
  * { margin: 0; padding: 0; box-sizing: border-box; }
  html, body { width: 852px; height: 1200px; overflow: hidden; background: var(--ink); }
  .flyer { position: relative; width: 852px; height: 1200px; background: var(--ink); }
  .parchment {
    position: absolute; left: 69px; top: 60px; width: 713px; height: 1083px;
    background: radial-gradient(ellipse at 50% 40%, var(--parchment-light) 0%, #ead0a0 55%, var(--parchment-dark) 100%);
  }
  .dots { position: absolute; inset: 0; }
  .art { position: absolute; }
  .art--stars { background: radial-gradient(ellipse at 40% 40%, rgba(239,154,28,0.45), rgba(239,154,28,0) 70%); }
  .art--owl { background: radial-gradient(ellipse, rgba(13,11,9,0.8) 40%, rgba(13,11,9,0) 70%); }
  .art--moon { background: radial-gradient(circle, var(--moon) 45%, rgba(246,227,168,0) 70%); }
  .art--paws { background: radial-gradient(ellipse, rgba(13,11,9,0.14), rgba(13,11,9,0) 70%); }
  .art--owls-pair {
    background: linear-gradient(90deg, rgba(20,16,12,0.8) 0%, rgba(20,16,12,0.8) 48%, rgba(236,150,60,0.8) 52%, rgba(245,190,110,0.8) 100%);
    border-radius: 45% 45% 20% 20%;
  }

  .presenter {
    position: absolute; left: 219px; top: 222px; width: 428px; height: 51px;
    background: var(--ink); border-radius: 26px;
    color: var(--orange); font-family: "Montserrat", sans-serif; font-weight: 800;
    font-size: 22px; line-height: 51px; text-align: center; letter-spacing: 0.3px;
  }
  .title-main {
    position: absolute; left: 0; width: 852px; top: 282px; text-align: center;
    font-family: "Cinzel", serif; font-weight: 700; font-size: 80px; line-height: 1; color: var(--ink); letter-spacing: 1px;
  }
  .title-line {
    position: absolute; left: 0; width: 852px; top: 378px; height: 190px;
    display: flex; justify-content: center; align-items: baseline; gap: 16px;
  }
  .title-small {
    font-family: "Cinzel", serif; font-weight: 500; font-size: 34px; color: var(--ink);
  }
  .title-script {
    font-family: "Great Vibes", cursive; font-size: 170px; line-height: 1.05; color: var(--orange);
  }
  .title-shadow {
    position: absolute; left: 358px; top: 580px; width: 135px; height: 20px; border-radius: 50%;
    background: radial-gradient(ellipse, var(--shadow), rgba(60,50,40,0) 70%);
  }
  .event-date {
    position: absolute; left: 0; width: 852px; top: 606px; text-align: center;
    font-family: "Oswald", sans-serif; font-weight: 700; font-size: 40px; line-height: 52px; color: var(--ink);
  }
  .event-venue {
    position: absolute; left: 0; width: 852px; top: 662px; text-align: center;
    font-family: "Oswald", sans-serif; font-weight: 600; font-size: 17px; line-height: 20px; letter-spacing: 0.4px;
    color: var(--ink); text-transform: uppercase;
  }
  .activities {
    position: absolute; left: 116px; top: 697px; list-style: none;
    font-family: "Montserrat", sans-serif; font-weight: 600; font-size: 14.5px; color: var(--ink);
  }
  .activities li { position: relative; padding-left: 22px; height: 26px; line-height: 26px; }
  .activities li::before {
    content: ""; position: absolute; left: 0; top: 7px; width: 12px; height: 12px; border-radius: 50%; background: var(--ink);
  }
  .college {
    position: absolute; left: 150px; top: 934px; display: flex; align-items: center; gap: 6px;
    font-family: "Montserrat", sans-serif; font-weight: 600; font-size: 10.5px; color: var(--logo-grey);
  }
  .college__dot { width: 16px; height: 16px; border-radius: 50%; border: 1.5px solid var(--logo-grey); }
</style>
</head>
<body>
<main class="flyer">
  <div class="parchment"></div>

  <svg class="dots" width="852" height="1200" aria-hidden="true">
    <g fill="#0d0b09">
      <circle cx="115" cy="110" r="12"/><circle cx="193" cy="94" r="6"/><circle cx="506" cy="112" r="6"/>
      <circle cx="744" cy="100" r="14"/><circle cx="100" cy="212" r="14"/><circle cx="90" cy="406" r="16"/>
      <circle cx="104" cy="332" r="6"/><circle cx="633" cy="338" r="6"/><circle cx="80" cy="957" r="15"/>
      <circle cx="101" cy="1088" r="6"/><circle cx="415" cy="1093" r="15"/><circle cx="495" cy="1100" r="6"/>
      <circle cx="760" cy="1030" r="15"/><circle cx="733" cy="1108" r="6"/><circle cx="776" cy="1130" r="10"/>
    </g>
  </svg>

  <div class="art art--stars" style="left:89px;top:93px;width:221px;height:200px" role="img" aria-label="Scattered orange stars"></div>
  <div class="art art--owl" style="left:397px;top:105px;width:100px;height:95px" role="img" aria-label="Fluffy owl with glowing eyes"></div>
  <div class="art art--moon" style="left:630px;top:140px;width:130px;height:120px" role="img" aria-label="Crescent moon"></div>

  <div class="presenter">STUDENT FORUM PRESENTS</div>
  <div class="title-main">LANTERN</div>
  <div class="title-line">
    <span class="title-small">walk for</span>
    <span class="title-script">Kids</span>
  </div>
  <div class="title-shadow"></div>

  <div class="art art--owl" style="left:110px;top:470px;width:70px;height:66px" role="img" aria-label="Small owl with glowing eyes"></div>
  <div class="art art--moon" style="left:675px;top:545px;width:64px;height:60px" role="img" aria-label="Small crescent moon"></div>

  <div class="event-date">FRIDAY&nbsp; OCT 25TH 2019</div>
  <div class="event-venue">Morrow Hall (Ground Floor)</div>

  <ul class="activities">
    <li>(Glowing) Footsteps showing the path the</li>
    <li>kids should go?</li>
    <li>Face painting</li>
    <li>Cotton Candy</li>
    <li>Fog Machine w/bubbles</li>
    <li>Candy sponsorship (Fairlot or Oak Basket)</li>
    <li>Encouraging the community to bring food</li>
    <li>donations for PRCC Food Pantry</li>
  </ul>

  <div class="college"><span class="college__dot"></span>Pellham Ridge Community College</div>

  <div class="art art--paws" style="left:98px;top:975px;width:347px;height:125px" role="img" aria-label="Trail of glowing footprints"></div>
  <div class="art art--owls-pair" style="left:488px;top:783px;width:220px;height:250px" role="img" aria-label="Dark owl and orange owl perched side by side"></div>
  <div class="art art--moon" style="left:712px;top:796px;width:56px;height:52px" role="img" aria-label="Small crescent moon"></div>
  <div class="art art--owl" style="left:436px;top:988px;width:62px;height:58px" role="img" aria-label="Small owl with glowing eyes"></div>
  <div class="art art--stars" style="left:560px;top:921px;width:212px;height:193px" role="img" aria-label="Scattered orange stars"></div>
</main>
</body>
</html>
```